Line of Premium Pelmeni and Perogies of supermarkets

A new company on the block looking for a unique design. A premium brand of perogies and pelmeni.
The price of the product is directed towards the upper to the middle class. the packaging price will be 20$ while you can find competitors at 8$, the packaging needs to reflect that.
attached is also the vector file of the logo of the company currently, it must be displayed prominently. (Dorvik)
there is a whole line of products, the design should be easily adjustable for different flavours.
the flavours are:
Perogies:
potato
potato/musrooms
cottage cheese
potato/feta/parsley
mushrooms/beef
Dumplings (pemini) :
veal
veal/chicken
chicken
veal/pork
chicken/veal/pork
the product uses the most quality meat and hand-made quality.
we are looking for a premium feel and a unique design that stands out.
please refer to the example of similar products we like, and please be as creative as you can.
we really like the one example, where the flavour (beef for instance) where the cow is the shape of the window.
we are looking for talented designers who are able to think outside of the (pelmeni) box.

```html
<!DOCTYPE html>
<html lang="en">
<head>
<meta charset="utf-8">
<title>Dorvik Perogies – Potato</title>
<link rel="stylesheet" href="https://fonts.googleapis.com/css2?family=Great+Vibes&family=Josefin+Sans:wght@400;600&family=Tenor+Sans&display=swap">
<style>
  :root {
    --bg: #ffffff;
    --pack-black: #0b0908;
    --glow-brown: #6b5446;
    --gold-dark: #9a7326;
    --gold-mid: #d9b163;
    --gold-light: #f6e2a6;
    --band-text: #3a2a12;
    --cream: #f2ece4;
    --food-light: #efe2c8;
    --food-dark: #b8864c;
    --herb: #4d7a2c;
  }
  * { margin: 0; padding: 0; box-sizing: border-box; }
  html, body { width: 1200px; height: 1155px; overflow: hidden; background: var(--bg); }
  .canvas { position: relative; width: 1200px; height: 1155px; }

  .pack {
    position: absolute; left: 300px; top: 60px; width: 600px; height: 1040px;
    background: var(--pack-black);
    overflow: hidden;
  }
  .pack-glow {
    position: absolute; left: 50%; top: 600px; width: 560px; height: 820px;
    transform: translate(-50%, -50%);
    background: radial-gradient(ellipse at center, var(--glow-brown) 0%, rgba(107,84,70,0.55) 35%, rgba(11,9,8,0) 70%);
  }

  .gold-band {
    position: absolute; left: 0; width: 100%;
    background: linear-gradient(90deg, var(--gold-dark), var(--gold-mid) 25%, var(--gold-light) 50%, var(--gold-mid) 75%, var(--gold-dark));
  }
  .top-band { top: 50px; height: 96px; display: flex; flex-direction: column; justify-content: space-around; padding: 6px 0; }
  .top-band span {
    font-family: "Josefin Sans", sans-serif; font-weight: 600; font-size: 19px;
    letter-spacing: 2px; color: var(--band-text); white-space: nowrap; text-align: center;
  }

  .label-band {
    top: 460px; height: 44px; display: flex; justify-content: space-between; align-items: center;
    padding: 0 30px;
  }
  .label-band span {
    font-family: "Josefin Sans", sans-serif; font-size: 21px; letter-spacing: 2px; color: var(--band-text);
  }

  .brand {
    position: absolute; left: 50%; top: 482px; transform: translate(-50%, -50%);
    width: 200px; height: 200px; border-radius: 50%;
    background: var(--cream);
    display: flex; align-items: center; justify-content: center;
  }
  .brand-name {
    font-family: "Josefin Sans", sans-serif; font-weight: 600; font-size: 34px;
    letter-spacing: 2px; color: var(--band-text);
  }

  .product-name {
    position: absolute; left: 0; width: 100%; top: 596px; text-align: center;
    font-family: "Great Vibes", cursive; font-weight: 400; font-size: 118px; line-height: 1;
    background: linear-gradient(180deg, var(--gold-light), var(--gold-mid) 50%, var(--gold-dark));
    -webkit-background-clip: text; background-clip: text; color: transparent;
  }

  .food-photo {
    position: absolute; left: 145px; top: 745px; width: 310px; height: 180px;
    border-radius: 40% 40% 30% 30%;
    background: radial-gradient(ellipse at 40% 45%, var(--food-light) 0%, var(--food-dark) 60%, rgba(184,134,76,0) 78%),
                radial-gradient(ellipse at 85% 35%, var(--herb) 0%, rgba(77,122,44,0) 35%);
  }

  .flavour-block {
    position: absolute; left: 0; width: 100%; top: 940px;
    display: flex; flex-direction: column; align-items: center;
  }
  .flavour-rule {
    display: block; height: 2px; width: 330px;
    background: linear-gradient(90deg, rgba(217,177,99,0), var(--gold-mid), rgba(217,177,99,0));
  }
  .flavour-name {
    display: block; margin: 12px 0; line-height: 1; text-align: center;
    font-family: "Tenor Sans", sans-serif; font-size: 34px; letter-spacing: 3px; color: var(--cream);
  }
</style>
</head>
<body>
  <div class="canvas">
    <section class="pack">
      <div class="pack-glow"></div>

      <div class="gold-band top-band">
        <span>LITY PREMIUM QUALITY PREMIUM QUALITY PRE</span>
        <span>UM QUALITY PREMIUM QUALITY PREMIUM QU</span>
        <span>TY PREMIUM QUALITY PREMIUM QUALITY PR</span>
      </div>

      <div class="gold-band label-band">
        <span>PREMIUM</span>
        <span>QUALITY</span>
      </div>

      <div class="brand"><span class="brand-name">Dorvik</span></div>

      <h1 class="product-name">Perogies</h1>

      <div class="food-photo" role="img" aria-label="Photo of golden pan-fried potato perogies stacked with a sprig of fresh parsley"></div>

      <div class="flavour-block">
        <span class="flavour-rule"></span>
        <span class="flavour-name">POTATO</span>
        <span class="flavour-rule"></span>
      </div>
    </section>
  </div>
</body>
</html>
```